Business Card Design

I am starting my therapy private practice. I will be an in home therapist, so I go into family's homes instead of using an office to do family/marriage therapy. Therefore, I do not have an office address. I am looking for something in the black, red, gray, and blue color scheme that appeals to both families, couples and teenagers.

Industry/Entity Type

Business

Contact Information for Business Card

Lena Brightwell, MS, MFT Intern
Marriage and Family Therapy
In Home Therapist
617-482-5190
Lena@LenaBrightwell-example.com

```html
<!DOCTYPE html>
<html lang="en">
<head>
<meta charset="utf-8">
<title>Lena Brightwell – Business Card</title>
<link rel="stylesheet" href="https://fonts.googleapis.com/css2?family=Open+Sans:wght@400;700&display=swap">
<style>
  :root {
    --ink-black: #14171c;
    --slate-gray: #3a4350;
    --steel-blue: #2c5d8f;
    --sky-blue: #5f8fbf;
    --mist-gray: #9aa7b5;
    --accent-red: #ff4b4b;
    --text-white: #ffffff;
  }
  html, body {
    margin: 0;
    padding: 0;
    width: 1200px;
    height: 722px;
    overflow: hidden;
    background: #ffffff;
  }
  .card {
    position: relative;
    width: 1200px;
    height: 722px;
    overflow: hidden;
    font-family: "Open Sans", "Segoe UI", sans-serif;
    color: var(--text-white);
  }
  .card__photo {
    position: absolute;
    inset: 0;
    background:
      radial-gradient(ellipse 420px 360px at 760px 420px, rgba(95, 143, 191, 0.55), rgba(95, 143, 191, 0) 70%),
      radial-gradient(ellipse 300px 260px at 1050px 250px, rgba(154, 167, 181, 0.35), rgba(154, 167, 181, 0) 70%),
      linear-gradient(100deg, var(--ink-black) 0%, var(--slate-gray) 38%, var(--steel-blue) 75%, var(--slate-gray) 100%);
  }
  .card__credentials {
    position: absolute;
    left: 437px;
    top: 126px;
    margin: 0;
    font-size: 38px;
    line-height: 57px;
    font-weight: 400;
  }
  .card__credentials-degree {
    color: var(--accent-red);
    font-weight: 700;
  }
  .card__name {
    position: absolute;
    left: 124px;
    top: 428px;
    margin: 0;
    font-size: 70px;
    line-height: 84px;
    font-weight: 400;
    letter-spacing: -0.5px;
  }
  .card__contact {
    position: absolute;
    left: 126px;
    top: 530px;
    margin: 0;
    font-size: 26px;
    line-height: 37px;
    font-weight: 400;
    font-style: normal;
  }
  .card__contact span { display: block; }
</style>
</head>
<body>
  <main class="card">
    <div class="card__photo" role="img" aria-label="Blue-gray toned photograph of a therapist's hands supporting a client's knee during an in-home session"></div>

    <p class="card__credentials">
      <span class="card__credentials-degree">MS, MFT</span> Intern Marriage and<br>
      Family Therapy In Home Therapist
    </p>

    <h1 class="card__name">Lena Brightwell</h1>

    <address class="card__contact">
      <span class="card__email">Lena@LenaBrightwell-example.com</span>
      <span class="card__phone">617-482-5190</span>
    </address>
  </main>
</body>
</html>
```